Vorel constructions

We are predominantly a residential home builder based in Melbourne, Victoria Australia. We construct houses, apartments, townhouses, multi-unit developments.

The name of the company is "Vorel Constructions"
My company believes in building unique construction projects mainly residential homes. The target customers are upmarket Melbourne residents/investors.

I want the brand name "Vorel" to be part of the logo. There's no need to put the word construction in the logo at this stage.

I would also like some ideas for a slogan e.g. "Just build it." or "We build quality homes." But I would like something unique and different for a slogan not the same old cliche.

vorelconstructions.example.com.au
e: tmelo@vorelconstructions.example.com.au
M: 0417305862
Address: 8/3 Fenwick Lane Brindale VIC 3990

Director:Mr Dinesh Malarkodiyan

```html
<!DOCTYPE html>
<html lang="en">
<head>
<meta charset="utf-8">
<title>Vorel Constructions – Business Card</title>
<link rel="stylesheet" href="https://fonts.googleapis.com/css2?family=Didact+Gothic&family=Mulish:wght@700;800&display=swap">
<style>
  :root {
    --page: #1c1c1f;
    --card: #2b2650;
    --accent: #1fa6dc;
    --ink: #d9d9e4;
    --white: #ffffff;
    --rule: #cfcfd8;
  }
  html, body {
    margin: 0;
    width: 1200px;
    height: 1000px;
    overflow: hidden;
    background: var(--page);
  }
  .business-card {
    position: absolute;
    left: 100px;
    top: 195px;
    width: 1000px;
    height: 611px;
    background: var(--card);
    box-shadow: 0 20px 50px rgba(0,0,0,0.5);
    font-family: "Didact Gothic", sans-serif;
    color: var(--ink);
  }
  .brand {
    position: absolute;
    left: 40px;
    width: 330px;
    top: 215px;
    text-align: center;
  }
  .brand-name {
    display: flex;
    align-items: center;
    justify-content: center;
    gap: 14px;
    font-family: "Didact Gothic", sans-serif;
    font-size: 92px;
    line-height: 1;
    color: var(--accent);
  }
  .brand-mark {
    width: 22px;
    height: 22px;
    background: var(--accent);
  }
  .brand-web {
    margin-top: 26px;
    font-family: "Mulish", sans-serif;
    font-weight: 800;
    font-size: 19px;
    color: var(--ink);
    white-space: nowrap;
  }
  .divider {
    position: absolute;
    left: 395px;
    top: 40px;
    width: 3px;
    height: 460px;
    background: var(--rule);
  }
  .person {
    position: absolute;
    left: 430px;
    top: 52px;
    width: 520px;
  }
  .person-name {
    margin: 0;
    font-family: "Mulish", sans-serif;
    font-weight: 800;
    font-size: 29px;
    color: var(--accent);
  }
  .person-title {
    margin: 2px 0 0;
    text-align: right;
    font-family: "Mulish", sans-serif;
    font-weight: 700;
    font-size: 19px;
    color: var(--white);
  }
  .contact-list {
    position: absolute;
    left: 432px;
    top: 225px;
    margin: 0;
    padding: 0;
    list-style: none;
    font-size: 25px;
    line-height: 1.15;
  }
  .contact-item {
    display: flex;
    align-items: flex-start;
    gap: 18px;
    margin-bottom: 36px;
  }
  .contact-icon {
    flex: none;
    width: 26px;
    height: 26px;
    margin-top: 4px;
    fill: var(--accent);
  }
  .address-line {
    display: block;
  }
  .address-line + .address-line {
    padding-left: 6px;
  }
</style>
</head>
<body>
  <section class="business-card">
    <div class="brand">
      <div class="brand-name"><span class="brand-mark"></span>Vorel</div>
      <div class="brand-web">vorelconstructions.example.com.au</div>
    </div>

    <div class="divider"></div>

    <header class="person">
      <h1 class="person-name">Mr Dinesh Malarkodiyan</h1>
      <p class="person-title">Director</p>
    </header>

    <ul class="contact-list">
      <li class="contact-item">
        <svg class="contact-icon" viewBox="0 0 24 24" aria-hidden="true"><path d="M12 3 2 12h3v9h5v-6h4v6h5v-9h3z"/></svg>
        <span><span class="address-line">8/3 Fenwick Lane</span><span class="address-line">Brindale VIC 3990</span></span>
      </li>
      <li class="contact-item">
        <svg class="contact-icon" viewBox="0 0 24 24" aria-hidden="true"><path d="M6.6 10.8a15 15 0 0 0 6.6 6.6l2.2-2.2a1 1 0 0 1 1-.25 11.4 11.4 0 0 0 3.6.57 1 1 0 0 1 1 1V20a1 1 0 0 1-1 1A17 17 0 0 1 3 4a1 1 0 0 1 1-1h3.5a1 1 0 0 1 1 1c0 1.25.2 2.450.57 3.57a1 1 0 0 1-.25 1z"/></svg>
        <span>0417305862</span>
      </li>
      <li class="contact-item">
        <svg class="contact-icon" viewBox="0 0 24 24" aria-hidden="true"><path d="M2 5h20v14H2zm2 2v.5l8 5 8-5V7zm0 2.8V17h16V9.8l-8 5z"/></svg>
        <span>tmelo@vorelconstructions.example.com.au</span>
      </li>
    </ul>
  </section>
</body>
</html>
```